Visitenkarten-Design für aufstrebendes, modernes und innovatives Elektrounternehmen
Zielgruppe
Unsere Firma ist im Bereich Elektro- und Gebäudetechnik angesiedelt.
Zielgruppe sind Privatkunden und Geschäftskunden.
Wir machen alles rund um das Thema Elektrotechnik, Elektroinstallation ....
Aufgabenstellung
Es soll ein ansprechendes modernes Design sein. Gerne auch mit Rückseite.
Wir sind ein junges aufstrebendes modernes und innovatives Unternehmen

```html
<!DOCTYPE html>
<html lang="de">
<head>
<meta charset="utf-8">
<title>Velmor Visitenkarte</title>
<link href="https://fonts.googleapis.com/css2?family=Saira+Semi+Condensed:wght@400;500;700&display=swap" rel="stylesheet">
<style>
  :root {
    --bg: #5e5e5e;
    --card: #ffffff;
    --olive: #c4b832;
    --teal: #1a9bb0;
    --graphite: #5b5c5e;
    --footer: #646567;
    --text: #2e2e2e;
    --watermark: #f1f1f1;
  }
  * { margin: 0; padding: 0; box-sizing: border-box; }
  html, body { width: 1200px; height: 1200px; overflow: hidden; }
  body {
    background: var(--bg);
    font-family: "Saira Semi Condensed", "Arial Narrow", sans-serif;
    position: relative;
  }
  .card {
    position: absolute;
    background: var(--card);
    overflow: hidden;
  }
  .card--front { left: 221px; top: 66px; width: 765px; height: 467px; }
  .card--back { left: 222px; top: 623px; width: 768px; height: 466px; }

  .watermark-circle {
    position: absolute;
    border-radius: 50%;
    background: var(--watermark);
  }
  .card--front .watermark-circle { left: 204px; top: 44px; width: 378px; height: 378px; }
  .card--back .watermark-circle { left: 195px; top: 43px; width: 380px; height: 380px; }

  .brand-mark {
    position: absolute;
    left: 106px; top: 166px;
    width: 136px; height: 136px;
    border-radius: 50%;
    background: var(--olive);
  }
  .brand-name {
    position: absolute;
    left: 262px; top: 162px;
    font-weight: 700;
    font-size: 112px;
    line-height: 1;
    color: var(--graphite);
    letter-spacing: 1px;
    white-space: nowrap;
  }
  .brand-tagline {
    position: absolute;
    left: 292px; top: 268px;
    font-weight: 700;
    font-size: 23px;
    line-height: 1;
    color: var(--teal);
    white-space: nowrap;
  }

  .name-band {
    position: absolute;
    left: 0; top: 0;
    width: 100%; height: 186px;
    background: var(--olive);
  }
  .person-name {
    position: absolute;
    left: 0; top: 56px; width: 100%;
    text-align: center;
    color: #fff;
    font-weight: 500;
    font-size: 48px;
    line-height: 1;
    letter-spacing: 2px;
    white-space: nowrap;
  }
  .person-title {
    position: absolute;
    left: 50%; top: 120px;
    transform: translateX(-50%);
    height: 35px;
    padding: 0 14px;
    background: var(--graphite);
    color: #fff;
    font-size: 18px;
    line-height: 35px;
    letter-spacing: 1px;
    white-space: nowrap;
  }
  .footer-band {
    position: absolute;
    left: 0; bottom: 0;
    width: 100%; height: 37px;
    background: var(--footer);
  }

  .contact {
    position: absolute;
    display: flex; align-items: center;
    color: var(--text);
    font-size: 18px;
    line-height: 1.25;
    white-space: nowrap;
  }
  .contact__icon {
    width: 42px; height: 42px;
    border-radius: 50%;
    background: var(--teal);
    display: flex; align-items: center; justify-content: center;
    flex-shrink: 0;
    margin-right: 22px;
  }
  .contact--address { left: 80px; top: 243px; }
  .contact--phone { left: 80px; top: 303px; }
  .contact--email { left: 413px; top: 237px; }
  .contact--web { left: 413px; top: 303px; }
</style>
</head>
<body>

<section class="card card--front">
  <div class="watermark-circle"></div>
  <div class="brand-mark"></div>
  <div class="brand-name">velmor</div>
  <div class="brand-tagline">ELEKTRO- &amp; GEBÄUDETECHNIK</div>
</section>

<section class="card card--back">
  <div class="watermark-circle"></div>
  <div class="name-band">
    <h1 class="person-name">TOBIAS VELMOR</h1>
    <div class="person-title">ELEKTROTECHNIKERMEISTER</div>
  </div>

  <div class="contact contact--address">
    <span class="contact__icon">
      <svg width="20" height="24" viewBox="0 0 20 24"><path d="M10 1a8 8 0 0 0-8 8c0 6 8 14 8 14s8-8 8-14a8 8 0 0 0-8-8z" fill="#fff"/><circle cx="10" cy="9" r="3" fill="#1a9bb0"/></svg>
    </span>
    <span>Lindenweg 12<br>80001 Musterfeld</span>
  </div>

  <div class="contact contact--phone">
    <span class="contact__icon">
      <svg width="22" height="22" viewBox="0 0 24 24"><path d="M6.6 2.5l3 3.5-2 2.5c1.2 2.8 3.4 5 6.2 6.2l2.5-2 3.5 3-2 3.3C11 19 5 13 4 4.5z" fill="#fff"/></svg>
    </span>
    <span>01234 / 567890</span>
  </div>

  <div class="contact contact--email">
    <span class="contact__icon">
      <svg width="24" height="18" viewBox="0 0 24 18"><rect x="1" y="1" width="22" height="16" fill="none" stroke="#fff" stroke-width="1.5"/><path d="M1 1l11 9 11-9M1 17l8-7M23 17l-8-7" fill="none" stroke="#fff" stroke-width="1.5"/></svg>
    </span>
    <span>info@velmor-licht-elektro.de</span>
  </div>

  <div class="contact contact--web">
    <span class="contact__icon">
      <svg width="26" height="26" viewBox="0 0 26 26"><circle cx="13" cy="13" r="10" fill="none" stroke="#fff" stroke-width="1.4"/><ellipse cx="13" cy="13" rx="4.5" ry="10" fill="none" stroke="#fff" stroke-width="1.2"/><path d="M3 13h20M5 8h16M5 18h16" stroke="#fff" stroke-width="1.2"/></svg>
    </span>
    <span>www.velmor-elektrotechnik.de</span>
  </div>

  <div class="footer-band"></div>
</section>

</body>
</html>
```